Business Card Design Project

Dorran
Sales Manager

38700 Pellham Ave, Suite 415
Irvine, CA 92604

Tel: 626-555-0147
Fax: 888-555-0162
E-mail: dorran@plovetrix.com

Target Market(s)

We are the distributor and wholesaler, the business card design want to show we are a strong company.

Industry/Entity Type

Business

Colors

Designer to choose colors to be used in the design.

```html
<!DOCTYPE html>
<html lang="en">
<head>
<meta charset="utf-8">
<title>Plovetrix – Business Card</title>
<link rel="stylesheet" href="https://fonts.googleapis.com/css2?family=Open+Sans:wght@400;600;700&display=swap">
<style>
  :root {
    --page-bg: #e9e8e4;
    --card-top: #f7f6f3;
    --card-bottom: #ecebe7;
    --card-edge: #cfcdc8;
    --ink-dark: #3a3a3a;
    --ink-mid: #4a4a4a;
    --rule: #6d6d6d;
    --green-light: #8cc63f;
    --green-dark: #2e6f32;
    --white: #ffffff;
  }
  * { margin: 0; padding: 0; box-sizing: border-box; }
  html, body {
    width: 1200px; height: 768px; overflow: hidden;
    background: var(--page-bg);
    font-family: "Open Sans", Arial, sans-serif;
  }
  .canvas { position: relative; width: 1200px; height: 768px; }
  .card {
    position: absolute; left: 100px; top: 94px;
    width: 1000px; height: 580px;
    background: linear-gradient(180deg, var(--card-top), var(--card-bottom));
    border: 1px solid var(--card-edge);
    box-shadow: 0 10px 30px rgba(0,0,0,0.12);
    overflow: hidden;
  }
  .brand {
    position: absolute; right: 72px; top: 96px;
    display: flex; align-items: center; gap: 12px;
  }
  .brand-dot { width: 22px; height: 22px; border-radius: 50%; background: var(--green-light); flex: none; }
  .brand-name { font-size: 50px; font-weight: 700; color: var(--green-light); line-height: 1; letter-spacing: -0.5px; }
  .holder-name {
    position: absolute; left: 73px; top: 218px;
    font-size: 48px; font-weight: 700; color: var(--ink-dark); line-height: 1;
  }
  .name-rule {
    position: absolute; left: 73px; top: 282px; width: 853px; height: 2px;
    background: linear-gradient(90deg, var(--rule) 70%, rgba(109,109,109,0));
  }
  .holder-title {
    position: absolute; left: 73px; top: 300px;
    font-size: 37px; font-weight: 400; color: var(--ink-mid); line-height: 1;
  }
  .contact {
    position: absolute; right: 71px; top: 304px;
    text-align: right; color: var(--ink-dark); font-size: 23px; line-height: 32px;
  }
  .contact .address { margin-bottom: 10px; }
  .contact-line { display: flex; justify-content: flex-end; align-items: center; gap: 8px; }
  .contact-line svg { width: 18px; height: 18px; flex: none; }
  .band { position: absolute; left: 0; bottom: 0; width: 1000px; height: 40px; }
  .band-web {
    position: absolute; left: 50px; bottom: 8px;
    font-size: 20px; color: var(--white); line-height: 1;
  }
</style>
</head>
<body>
<main class="canvas">
  <section class="card">
    <div class="brand">
      <span class="brand-dot"></span>
      <span class="brand-name">Plovetrix</span>
    </div>

    <h1 class="holder-name">Dorran</h1>
    <div class="name-rule"></div>
    <p class="holder-title">Sales Manager</p>

    <div class="contact">
      <p class="address">38700 Pellham Ave, Suite 415<br>Irvine, CA 92604</p>
      <p class="contact-line">Tel: 626-555-0147
        <svg viewBox="0 0 24 24" aria-hidden="true"><path fill="#3a3a3a" d="M6.6 10.8a15 15 0 0 0 6.6 6.6l2.2-2.2c.3-.3.7-.4 1-.2 1.1.4 2.3.6 3.6.6.6 0 1 .4 1 1V20c0 .6-.4 1-1 1A17 17 0 0 1 3 4c0-.6.4-1 1-1h3.5c.6 0 1 .4 1 1 0 1.3.2 2.5.6 3.6.1.3 0 .7-.2 1z"/></svg>
      </p>
      <p class="contact-line">Fax: 888-555-0162
        <svg viewBox="0 0 24 24" aria-hidden="true"><g fill="#3a3a3a"><rect x="6" y="2" width="12" height="6" rx="1"/><rect x="2" y="9" width="20" height="9" rx="1.5"/><rect x="6" y="15" width="12" height="7" fill="#f2f1ee" stroke="#3a3a3a" stroke-width="1.6"/></g></svg>
      </p>
      <p class="contact-line">dorran@plovetrix.com
        <svg viewBox="0 0 24 24" aria-hidden="true"><rect x="2" y="5" width="20" height="14" rx="1.5" fill="#3a3a3a"/><path d="M3 6l9 7 9-7" fill="none" stroke="#f2f1ee" stroke-width="1.6"/></svg>
      </p>
      <p class="contact-line">www.plovetrix.com
        <svg viewBox="0 0 24 24" aria-hidden="true"><g fill="none" stroke="#3a3a3a" stroke-width="1.8"><circle cx="12" cy="12" r="9"/><ellipse cx="12" cy="12" rx="4" ry="9"/><path d="M3 12h18M5 7h14M5 17h14"/></g></svg>
      </p>
    </div>

    <svg class="band" viewBox="0 0 1000 40" preserveAspectRatio="none" aria-hidden="true">
      <rect x="390" y="0" width="610" height="40" fill="var(--green-dark)"/>
      <path d="M0 0 H350 C385 0 395 20 405 40 H0 Z" fill="var(--green-light)"/>
    </svg>
    <p class="band-web">www.plovetrix.com</p>
  </section>
</main>
</body>
</html>
```